Stationery Design Project

We are a start up wine business based in Sydney Australia. We already have a logo and are in the process of completing our website. We require our logo to be cleverly and artfully incorporated into our stationary requirements. Which will initially begin with a company letter head.
As we desire consistency across our brand, we will also be wanting to develop banner advertisements and brochure with the same "look".
If outstanding we move design brief to banner advertisement for web and banner of the website itself.
Older wealthy predominantly male demographic
Business

```html
<!DOCTYPE html>
<html lang="en">
<head>
<meta charset="utf-8">
<title>Vine Heritage Cellars – Stationery</title>
<link href="https://fonts.googleapis.com/css2?family=Questrial&display=swap" rel="stylesheet">
<style>
  :root {
    --backdrop: #4a4a4a;
    --paper: #e6dad0;
    --brown: #8a5a2f;
    --brown-deep: #6f4522;
    --ink: #2c2522;
    --accent: #b8743a;
    --cream: #f4ece3;
    --tan: #c9a477;
    --sand: #dfc7a6;
    --blush: #e3bfae;
  }
  * { box-sizing: border-box; margin: 0; padding: 0; }
  html, body { width: 1200px; height: 960px; overflow: hidden; }
  body {
    background: var(--backdrop);
    font-family: "Questrial", "Century Gothic", sans-serif;
    color: var(--ink);
    position: relative;
  }
  .piece { position: absolute; overflow: hidden; }
  .piece svg.swirl { position: absolute; left: 0; top: 0; }

  /* Letterhead */
  .letterhead { left: 62px; top: 79px; width: 568px; height: 803px; background: var(--paper); }
  .letterhead .brand {
    position: absolute; left: 34px; top: 30px; width: 100px;
    font-size: 13px; line-height: 1.2; color: var(--ink);
  }
  .letterhead .sender { position: absolute; left: 148px; top: 52px; font-size: 10px; line-height: 1.35; }
  .letterhead .sender .abn { color: var(--accent); }
  .letterhead .contact {
    position: absolute; left: 148px; top: 78px;
    display: grid; grid-template-columns: 92px auto; column-gap: 4px;
    font-size: 9px; line-height: 1.4;
  }
  .label { color: var(--accent); }
  .letterhead .rule { position: absolute; left: 148px; right: 0; top: 109px; height: 1px; background: #a79a90; }

  /* Vertical card */
  .card-front { left: 647px; top: 79px; width: 286px; height: 500px; background: var(--brown); }
  .card-front .brand {
    position: absolute; left: 0; right: 0; top: 130px; text-align: center;
    color: var(--cream); font-size: 26px; line-height: 1.15;
  }
  .card-front .web {
    position: absolute; left: 0; right: 0; top: 303px; text-align: center;
    color: var(--cream); font-size: 11px;
  }

  /* Horizontal card */
  .card-back { left: 647px; top: 594px; width: 503px; height: 288px; background: var(--brown); }
  .card-back .person { position: absolute; left: 36px; top: 80px; }
  .card-back .name { font-size: 17px; color: var(--brown-deep); }
  .card-back .position { font-size: 12px; margin-top: 3px; }
  .card-back .contact {
    position: absolute; left: 36px; top: 138px;
    font-size: 12px; line-height: 1.45;
  }
  .card-back .brand {
    position: absolute; left: 340px; top: 108px; width: 140px; text-align: center;
    color: var(--cream); font-size: 20px; line-height: 1.15;
  }
</style>
</head>
<body>

<section class="piece letterhead" aria-label="Letterhead">
  <svg class="swirl" width="568" height="803" viewBox="0 0 568 803" aria-hidden="true">
    <path d="M0 660 C150 560 420 560 568 610 L568 803 L0 803 Z" fill="var(--blush)" opacity="0.35"/>
    <path d="M0 700 C170 620 430 630 568 700 L568 803 L0 803 Z" fill="var(--sand)" opacity="0.55"/>
    <path d="M0 760 C180 700 420 700 568 740 L568 803 L0 803 Z" fill="var(--tan)" opacity="0.6"/>
    <path d="M300 803 C420 760 520 720 568 690 L568 803 Z" fill="var(--accent)" opacity="0.55"/>
    <path d="M0 790 C200 740 400 760 568 780" stroke="var(--cream)" stroke-width="3" fill="none" opacity="0.7"/>
  </svg>
  <div class="brand">Vine Heritage Cellars</div>
  <div class="sender">
    <div>CLAIRE HADLEY</div>
    <div><span class="abn">ABN NUMBER :</span> 0987654321</div>
  </div>
  <div class="contact">
    <span><span class="label">tel :</span> 0200 555 0148</span>
    <span><span class="label">email:</span> hello@vineheritagecellars.example</span>
    <span><span class="label">fax :</span> 0200 555 0199</span>
    <span><span class="label">web:</span> www.vineheritagecellars.example</span>
  </div>
  <div class="rule"></div>
</section>

<section class="piece card-front" aria-label="Business card front">
  <svg class="swirl" width="286" height="500" viewBox="0 0 286 500" aria-hidden="true">
    <path d="M0 345 C110 330 230 370 286 420 L286 500 L0 500 Z" fill="var(--tan)" opacity="0.35"/>
    <path d="M0 390 C120 375 230 420 286 470 L286 500 L0 500 Z" fill="var(--sand)" opacity="0.55"/>
    <path d="M0 440 C110 430 210 460 260 500 L0 500 Z" fill="var(--cream)" opacity="0.6"/>
    <path d="M0 365 C120 355 220 395 286 450" stroke="var(--cream)" stroke-width="2" fill="none" opacity="0.5"/>
  </svg>
  <div class="brand">Vine Heritage<br>Cellars</div>
  <div class="web">www.vineheritagecellars.example</div>
</section>

<section class="piece card-back" aria-label="Business card back">
  <svg class="swirl" width="503" height="288" viewBox="0 0 503 288" aria-hidden="true">
    <path d="M0 0 L250 0 C330 60 360 180 330 288 L0 288 Z" fill="var(--tan)" opacity="0.8"/>
    <path d="M0 0 L220 0 C300 70 320 180 300 288 L0 288 Z" fill="var(--sand)"/>
    <path d="M0 0 L190 0 C270 70 290 180 272 288 L0 288 Z" fill="var(--paper)"/>
    <path d="M240 0 C320 70 345 190 320 288" stroke="var(--cream)" stroke-width="2" fill="none" opacity="0.6"/>
  </svg>
  <div class="person">
    <div class="name">Claire Hadley</div>
    <div class="position">Position</div>
  </div>
  <div class="contact">
    <div><span class="label">tel :</span> 0200 555 0148</div>
    <div><span class="label">fax :</span> 0200 555 0199</div>
    <div><span class="label">email :</span> hello@vineheritagecellars.example</div>
    <div><span class="label">web :</span> www.vineheritagecellars.example</div>
  </div>
  <div class="brand">Vine Heritage<br>Cellars</div>
</section>

</body>
</html>
```